Wordpress Design Project for CLG

We need a clean word press design for a new event planning company called Marigold Gathering & Occasions. We assist planners or leaders who are in charge of planning conferences, meetings, or conventions. In addition, we offer small business development strategy. We do not decorate: we help clients negotiate better contracts and/ or develop better systems to become more efficient. I want people to come to this site for referrals for other businesses and for training information.
I would like to see a design that uses the colors in the logo. The final design should be creative, professional, and innovative.
Industry/Entity Type
Event Planning
Requirements
Must have
- user friendly! easy to Navigate!
I like the feel of the following websites:
http://www.ventureowls.com.au/
http://galatrove.com/
Obviously, I will need to grow to that size of a site but I love it...
1.Client Sign in portal-
2. Social media and blog friendly!! I want people to use the site on a regular. I will post video, articles, and social media daily.
visitors can sign up or in using social media
very open to suggestions
Landing page for site that allows visitor to decide what they want to visit (button)- should be catchy
a. Convention & Meeting Services
b. Social Events
c. Small Business Solutions
2. Tabs
a. Home (ability to have pic gallery rotating)
b. About CLG
c. Contact us
d. Convention & Meeting services
e. Social Events
f. Small Business Solutions
g. Testimonials
Nice to have
- Mobile friendly, very clean design

```html
<!DOCTYPE html>
<html lang="en">
<head>
<meta charset="utf-8">
<title>Marigold Gathering &amp; Occasions</title>
<link href="https://fonts.googleapis.com/css2?family=Open+Sans:ital,wght@0,400;0,600;0,700;1,400;1,600&family=Noto+Serif:wght@400&display=swap" rel="stylesheet">
<style>
:root{
  --header:#2e2d33;
  --nav:#8f7bd6;
  --nav-line:#7f6bc8;
  --purple:#7b6bc9;
  --red:#e3372a;
  --red-soft:#e9877c;
  --band:#e9e9ea;
  --panel:#f7f7f7;
  --border:#dcdcdc;
  --text:#5a5a5a;
  --dark:#333;
  --footer:#58585a;
  --bottom:#e6e6e6;
}
*{margin:0;padding:0;box-sizing:border-box}
html,body{width:897px;height:1200px;overflow:hidden}
body{position:relative;background:#fff;font-family:"Open Sans",Arial,sans-serif;color:var(--text)}
.abs{position:absolute}
.site-header{left:0;top:0;width:897px;height:97px;background:var(--header)}
.brand{left:104px;top:24px;display:flex;align-items:center;gap:10px}
.brand-mark{width:22px;height:22px;border-radius:50%;background:var(--purple)}
.brand-name{font-family:"Noto Serif",Georgia,serif;font-size:30px;color:var(--purple);line-height:1}
.brand-sub{left:136px;top:62px;font-size:11px;color:#b9b8bd;letter-spacing:.2px}
.call{right:97px;top:28px;text-align:right}
.call-label{font-family:"Noto Serif",Georgia,serif;font-size:13px;color:#fff}
.call-number{font-family:"Noto Serif",Georgia,serif;font-size:25px;color:var(--red);line-height:1.1}
.main-nav{left:0;top:97px;width:897px;height:36px;background:var(--nav);border-top:1px solid #a595e2}
.main-nav ul{position:absolute;left:97px;top:0;display:flex;list-style:none;height:35px}
.main-nav li{font-size:10px;font-weight:600;color:#fff;text-transform:uppercase;display:flex;align-items:center;justify-content:center;border-left:1px solid var(--nav-line)}
.main-nav li:first-child{border-left:none;justify-content:flex-start}
.slider-band{left:0;top:133px;width:897px;height:372px;background:linear-gradient(90deg,#e4e4e5,#f1f1f1 50%,#e4e4e5)}
.slide{left:97px;top:143px;width:703px;height:321px;background:#fff;padding:3px;box-shadow:0 6px 10px -6px rgba(0,0,0,.45)}
.slide-photo{width:100%;height:100%;background:linear-gradient(160deg,#6b3a26,#3a2019 45%,#8a3a2e 75%,#5b3128)}
.dots{left:413px;top:475px;display:flex;gap:7px}
.dot{width:12px;height:12px;border-radius:3px;background:var(--red-soft)}
.dot.on{background:var(--red)}
.panel{background:var(--panel);border:1px solid var(--border)}
.panel h2{font-family:"Noto Serif",Georgia,serif;font-weight:400;font-size:19px;color:var(--purple)}
.welcome{left:90px;top:518px;width:470px;height:192px;padding:12px 14px}
.welcome p{font-size:9.3px;line-height:17.3px;margin-top:8px;padding-left:3px}
.btn{display:inline-block;background:var(--red);color:#fff;font-size:10px;padding:3px 9px;border:1px solid #c42a1f}
.welcome .btn{position:absolute;left:17px;top:147px}
.what{left:90px;top:726px;width:470px;height:270px;padding:12px 14px}
.service{position:absolute;top:42px;width:130px}
.service-photo{width:130px;height:82px;border:3px solid #ddd}
.service h3{font-size:11.2px;font-weight:600;color:var(--red);margin-top:10px;line-height:14.4px}
.service p{font-size:9px;line-height:13.6px;margin-top:5px}
.service .btn{position:absolute;top:202px;left:0;padding:2px 12px}
.events{left:575px;top:518px;width:225px;height:237px;padding:9px 10px}
.arrows{position:absolute;right:8px;top:13px;display:flex;gap:3px}
.arrow{width:14px;height:14px;border-radius:50%;background:#ddd;display:flex;align-items:center;justify-content:center}
.event{position:absolute;left:8px;width:205px}
.date{position:absolute;left:0;top:0;width:47px;height:47px;border-radius:50%;background:var(--red);color:#fff;text-align:center;font-family:"Noto Serif",Georgia,serif}
.date .m{font-size:11px;display:block;margin-top:6px;line-height:1}
.date .d{font-size:19px;display:block;line-height:1.1}
.event p{margin-left:62px;font-size:9px;line-height:15px}
.event a{color:var(--red);font-weight:600;font-size:9px;text-decoration:none}
.view-all{position:absolute;left:15px;top:207px;font-size:9.5px;font-weight:600;color:var(--dark)}
.testimonials{left:575px;top:772px;width:225px;height:225px;padding:9px 10px}
.quote{position:absolute;left:10px;width:203px;font-size:9px;line-height:15px;font-style:italic}
.quote .q{font-family:"Noto Serif",Georgia,serif;font-style:normal;font-size:20px;color:#888;line-height:0;vertical-align:-6px;margin-right:4px}
.quote a{color:var(--red);text-decoration:none}
.quote .by{text-align:right;font-weight:600;color:var(--dark);margin-top:7px}
.divider{position:absolute;left:10px;width:203px;top:124px;border-top:1px solid #ccc}
.site-footer{left:0;top:1010px;width:897px;height:140px;background:var(--footer);color:#fff}
.footer-links{position:absolute;left:97px;top:14px;list-style:none;font-size:9px;line-height:17.2px}
.site-footer h4{position:absolute;font-size:10.5px;font-weight:600;letter-spacing:.3px}
.email{position:absolute;left:276px;top:37px;width:165px;height:28px;background:#fff;border:1px solid #ccc;font-size:9px;color:#999;padding:8px 9px}
.submit{position:absolute;left:381px;top:76px;width:60px;height:24px;background:var(--nav);font-size:10.5px;font-weight:600;text-align:center;line-height:24px}
.sponsor{position:absolute;top:32px;font-size:17px;color:#d8d8d8;letter-spacing:.5px}
.social{position:absolute;left:473px;top:102px;display:flex;gap:7px}
.social span{width:22px;height:22px;border-radius:3px}
.bottom-bar{left:0;top:1150px;width:897px;height:50px;background:var(--bottom);text-align:center;font-size:9px;line-height:50px;color:#777}
.bottom-bar em{font-style:normal;color:var(--red)}
</style>
</head>
<body>
<header class="site-header abs">
  <div class="brand abs"><span class="brand-mark"></span><span class="brand-name">Marigold</span></div>
  <div class="brand-sub abs">Gathering &amp; Occasions</div>
  <div class="call abs">
    <div class="call-label">Call Us</div>
    <div class="call-number">555 018 2240</div>
  </div>
</header>

<nav class="main-nav abs">
  <ul>
    <li style="width:53px">Home</li>
    <li style="width:212px">Convention &amp; Meeting Services</li>
    <li style="width:121px">Social Events</li>
    <li style="width:128px">Small Business</li>
    <li style="width:119px">Testimonials</li>
    <li style="width:70px;justify-content:flex-end">Contact</li>
  </ul>
</nav>

<section class="slider-band abs">
</section>
<div class="slide abs"><div class="slide-photo" role="img" aria-label="Crowd of guests mingling at a cinema lobby event with balloons"></div></div>
<div class="dots abs"><span class="dot on"></span><span class="dot"></span><span class="dot"></span><span class="dot"></span></div>

<section class="welcome panel abs">
  <h2>Welcome to Our Site</h2>
  <p>Aliquam molestie, mi et imperdiet euismod, dui purus auctor tellus, et interdum lacus lectus et ante. Sed accumsan sollicitudin sapien, sit amet adipiscing turpis gravida ac. In congue, neque ac lobortis volutpat, libero mauris varius mi, vitae suscipit ipsum ligula vitae risus. Duis aliquam nibh a dui iaculis viverra id a velit. Vivamus egestas risus in magna varius commodo. Sed semper viverra egestas. Etiam pretium porttitor lectus, vel ornare neque porta volutpat.</p>
  <span class="btn">Read More</span>
</section>

<section class="what panel abs">
  <h2>What We Do</h2>
  <div class="service" style="left:14px">
    <div class="service-photo" role="img" aria-label="Business people shaking hands in an office" style="background:linear-gradient(135deg,#cfd3d8,#5c6470)"></div>
    <h3>Convention &amp; Meeting Services</h3>
    <p>Aliquam molestie, mi et imperdiet euismod, dui purus auctor tellus, et interdum lacus lectus et ante.</p>
    <span class="btn">More</span>
  </div>
  <div class="service" style="left:169px">
    <div class="service-photo" role="img" aria-label="Friends toasting with champagne at a party" style="background:linear-gradient(135deg,#6a5040,#d9b48a)"></div>
    <h3>Social Events</h3>
    <p>Aliquam molestie, mi et imperdiet euismod, dui purus auctor tellus, et interdum lacus lectus et ante.</p>
    <span class="btn">More</span>
  </div>
  <div class="service" style="left:324px">
    <div class="service-photo" role="img" aria-label="Handshake in front of a world map" style="background:linear-gradient(135deg,#2c6fa3,#8fc3e0)"></div>
    <h3>Small Business</h3>
    <p>Aliquam molestie, mi et imperdiet euismod, dui purus auctor tellus, et interdum lacus lectus et ante.</p>
    <span class="btn">More</span>
  </div>
</section>

<aside class="events panel abs">
  <h2>Upcoming Events</h2>
  <div class="arrows">
    <span class="arrow"><svg width="6" height="6"><path d="M5 0L1 3 5 6z" fill="#333"/></svg></span>
    <span class="arrow"><svg width="6" height="6"><path d="M1 0L5 3 1 6z" fill="#333"/></svg></span>
  </div>
  <div class="event" style="top:40px">
    <div class="date"><span class="m">May</span><span class="d">05</span></div>
    <p>Aliquam molestie, mi et imperdiet euismod, dui purus auctor tellus, et interdum lacus lectus et ante.<br><a>Read More</a></p>
  </div>
  <div class="event" style="top:123px">
    <div class="date"><span class="m">May</span><span class="d">05</span></div>
    <p>Aliquam molestie, mi et imperdiet euismod, dui purus auctor tellus, et interdum lacus lectus et ante.<br><a>Read More</a></p>
  </div>
  <span class="view-all">VIEW ALL EVENTS</span>
</aside>

<aside class="testimonials panel abs">
  <h2>Testimonials</h2>
  <div class="arrows">
    <span class="arrow"><svg width="6" height="6"><path d="M5 0L1 3 5 6z" fill="#333"/></svg></span>
    <span class="arrow"><svg width="6" height="6"><path d="M1 0L5 3 1 6z" fill="#333"/></svg></span>
  </div>
  <div class="quote" style="top:37px">
    <span class="q">&ldquo;</span>Vestibulum ante ipsum primis in faucibus orci luctus et ultrices posuere cubilia Curae. Aenean a nibh eget turpis vehicula tempus ac sed massa. <a>Read More</a>
    <div class="by">By &nbsp;Dana Ellery</div>
  </div>
  <div class="divider"></div>
  <div class="quote" style="top:136px">
    <span class="q">&ldquo;</span>Vestibulum ante ipsum primis in faucibus orci luctus et ultrices posuere cubilia Curae. Aenean a nibh eget turpis vehicula tempus ac sed massa. <a>Read More</a>
    <div class="by">By &nbsp;Dana Ellery</div>
  </div>
</aside>

<footer class="site-footer abs">
  <ul class="footer-links">
    <li>Home</li><li>About CLG</li><li>Convention &amp; Meeting Services</li><li>Social Events</li><li>Small Business Solutions</li><li>Testimonials</li><li>Contact Us</li>
  </ul>
  <h4 style="left:276px;top:14px">NEWSLETTER SIGN UP</h4>
  <div class="email">Enter Email</div>
  <div class="submit">SUBMIT</div>
  <h4 style="left:473px;top:14px">SPONSORS</h4>
  <span class="sponsor" style="left:473px">LUMORA</span>
  <span class="sponsor" style="left:589px">harborline</span>
  <span class="sponsor" style="left:693px;font-weight:700">Brightway</span>
  <h4 style="left:473px;top:78px">CONNECT US</h4>
  <div class="social">
    <span style="background:#3b5a9a"></span>
    <span style="background:#3fa9d8"></span>
    <span style="background:#e8781e"></span>
    <span style="background:#c4262b"></span>
  </div>
</footer>

<div class="bottom-bar abs">Copyright &copy; 2013. <em>Marigold Gathering &amp; Occasions.</em> All Right Reserved</div>
</body>
</html>
```